Update Pulp Pantry menu board to appear Fresh and modern

I need a menu board design that is not cluttered, easy to read, playful and the style of healthy and fresh for a juice bar. I will be editing the details of the items, so basically the design is all I need. I prefer the files to be in Microsoft Publisher as I am most familiar, but I have illustrator as well, but not as advanced on that. The size should be 36"x36". I will create 3 seperate boards from the one design.

Target Market(s)

health concious people, active lifestyle people

Font styles to use
Serif

Colors

Designer to choose colors to be used in the design.

Requirements
Must have
• Not cluttered
• Modern feel
Nice to have
• i like the style of the
• "cold pressed juice" part of my attached juice bottle label

```html
<!DOCTYPE html>
<html lang="en">
<head>
<meta charset="utf-8">
<title>Pulp Pantry — Menu Board</title>
<link rel="stylesheet" href="https://fonts.googleapis.com/css2?family=Archivo:wdth,wght@75..100,800..900&family=Archivo+Black&family=Rammetto+One&family=Montserrat:wght@600&family=Noto+Sans:wght@400&display=swap">
<style>
  :root {
    --orange: #f26a22;
    --orange-light: #f9a45a;
    --charcoal: #4d4d4d;
    --cream: #fdebe0;
    --cream-soft: #fdf2ea;
    --cream-frame: rgba(253, 235, 224, 0.3);
    --white: #ffffff;
  }
  * { margin: 0; padding: 0; box-sizing: border-box; }
  html, body { width: 1200px; height: 1200px; overflow: hidden; background: var(--white); }
  .board { position: relative; width: 1200px; height: 1200px; overflow: hidden; background: var(--white); }

  /* Header */
  .brand { position: absolute; left: 0; top: 0; width: 1200px; height: 227px; }
  .brand-dot { position: absolute; left: 309px; top: 46px; width: 162px; height: 162px; border-radius: 50%; background: var(--charcoal); }
  .brand-name {
    position: absolute; left: 486px; top: 40px;
    font-family: "Montserrat", sans-serif; font-weight: 600;
    color: var(--orange); font-size: 82px; line-height: 88px; letter-spacing: 1px;
  }
  .top-bar { position: absolute; left: 0; top: 227px; width: 1198px; height: 22px; background: var(--charcoal); }

  /* Backdrop */
  .backdrop {
    position: absolute; left: 0; top: 249px; width: 1200px; height: 929px;
    background:
      radial-gradient(circle at 8% 78%, var(--orange-light) 0, rgba(249,164,90,0) 38%),
      radial-gradient(circle at 88% 30%, var(--orange-light) 0, rgba(249,164,90,0) 36%),
      radial-gradient(circle at 62% 104%, var(--orange-light) 0, rgba(249,164,90,0) 28%),
      var(--orange);
  }
  .bottom-bar { position: absolute; left: 0; top: 1178px; width: 1200px; height: 22px; background: var(--charcoal); }

  .panel-frame { position: absolute; left: 93px; top: 252px; width: 1035px; height: 850px; border-radius: 12px; background: var(--cream-frame); }
  .panel {
    position: absolute; left: 110px; top: 270px; width: 1000px; height: 801px;
    background:
      radial-gradient(circle at 85% 20%, var(--cream-soft) 0, rgba(253,242,234,0) 35%),
      radial-gradient(circle at 10% 75%, var(--cream-soft) 0, rgba(253,242,234,0) 40%),
      var(--cream);
  }

  /* Menu sections */
  .menu-section { position: absolute; color: var(--charcoal); }
  .section-title {
    font-family: "Archivo", sans-serif; font-weight: 900; font-stretch: 80%;
    color: var(--orange); font-size: 60px; line-height: 52px; letter-spacing: -1.5px;
    white-space: nowrap;
  }
  .section-tagline {
    font-family: "Rammetto One", sans-serif; font-size: 21px; line-height: 24px;
    color: var(--charcoal); margin-top: 2px; white-space: nowrap;
  }
  .section-rule { height: 10px; background: var(--orange); margin-top: 16px; }

  .size-head, .menu-item-head {
    display: grid; grid-template-columns: 1fr 51px 51px 51px; align-items: end;
  }
  .size-head { margin-top: 8px; font-family: "Archivo Black", sans-serif; font-size: 15px; line-height: 16px; }
  .size-head span, .price { text-align: center; }
  .menu-item { height: 88px; }
  .menu-item-head { font-family: "Archivo Black", sans-serif; font-size: 26px; line-height: 30px; letter-spacing: -1px; }
  .price { font-size: 26px; letter-spacing: -0.5px; }
  .item-desc {
    font-family: "Noto Sans", sans-serif; font-size: 22px; line-height: 25px;
    letter-spacing: 1px; padding-left: 17px; white-space: nowrap;
  }

  .juices { left: 140px; top: 296px; width: 408px; }
  .smoothies { left: 683px; top: 296px; width: 405px; }
  .smoothies .section-title { padding-left: 7px; }
  .smoothies .section-tagline { padding-left: 10px; }
  .smoothies .size-head { margin-top: 6px; }
  .shots { left: 140px; top: 832px; width: 400px; }

  .shot-list { list-style: none; margin-top: 14px; }
  .shot-item {
    display: grid; grid-template-columns: 1fr 64px;
    font-family: "Archivo Black", sans-serif; font-size: 26px; line-height: 34.5px; letter-spacing: -1px;
  }
</style>
</head>
<body>
<div class="board">

  <header class="brand">
    <div class="brand-dot"></div>
    <div class="brand-name">PULP<br>PANTRY</div>
  </header>
  <div class="top-bar"></div>

  <div class="backdrop" role="img" aria-label="Illustration of large citrus slices and green leaves across the orange background"></div>
  <div class="bottom-bar"></div>

  <div class="panel-frame"></div>
  <div class="panel" role="img" aria-label="Faint citrus slice and leaf illustration behind the menu text"></div>

  <section class="menu-section juices">
    <h2 class="section-title">FRUIT JUICES</h2>
    <p class="section-tagline">pick your squeeze!</p>
    <div class="section-rule"></div>
    <div class="size-head"><span></span><span>SM</span><span>MD</span><span>LG</span></div>
    <div class="menu-item">
      <div class="menu-item-head"><span>Mango Madness</span><span class="price">8</span><span class="price">10</span><span class="price">12</span></div>
      <p class="item-desc">Lorem ipsum dolor sit amet,<br>consectetuer adipiscing elit.</p>
    </div>
    <div class="menu-item">
      <div class="menu-item-head"><span>Go GREEN!</span><span class="price">8</span><span class="price">10</span><span class="price">12</span></div>
      <p class="item-desc">Lorem ipsum dolor sit amet,<br>consectetuer adipiscing elit..</p>
    </div>
    <div class="menu-item">
      <div class="menu-item-head"><span>Pinapple</span><span class="price">8</span><span class="price">10</span><span class="price">12</span></div>
      <p class="item-desc">Lorem ipsum dolor sit amet,<br>consectetuer adipiscing elit..</p>
    </div>
    <div class="menu-item">
      <div class="menu-item-head"><span>Tropic</span><span class="price">8</span><span class="price">10</span><span class="price">12</span></div>
      <p class="item-desc">Lorem ipsum dolor sit amet,<br>consectetuer adipiscing elit.</p>
    </div>
  </section>

  <section class="menu-section shots">
    <h2 class="section-title">SHOTS</h2>
    <p class="section-tagline">6 oz. pour</p>
    <div class="section-rule" style="width:400px"></div>
    <ul class="shot-list">
      <li class="shot-item"><span>Wheatgrass</span><span>5.50</span></li>
      <li class="shot-item"><span>Kale</span><span>6.75</span></li>
      <li class="shot-item"><span>Kombucha</span><span>4.75</span></li>
    </ul>
  </section>

  <section class="menu-section smoothies">
    <h2 class="section-title">SMOOTHIES</h2>
    <p class="section-tagline">pick your blend!</p>
    <div class="section-rule"></div>
    <div class="size-head"><span></span><span>SM</span><span>MD</span><span>LG</span></div>
    <div class="menu-item">
      <div class="menu-item-head"><span>Mango Madness</span><span class="price">8</span><span class="price">10</span><span class="price">12</span></div>
      <p class="item-desc">Lorem ipsum dolor sit amet,<br>consectetuer adipiscing elit.</p>
    </div>
    <div class="menu-item">
      <div class="menu-item-head"><span>Strawberry</span><span class="price">8</span><span class="price">10</span><span class="price">12</span></div>
      <p class="item-desc">Lorem ipsum dolor sit amet,<br>consectetuer adipiscing elit.</p>
    </div>
    <div class="menu-item">
      <div class="menu-item-head"><span>Lemon</span><span class="price">8</span><span class="price">10</span><span class="price">12</span></div>
      <p class="item-desc">Lorem ipsum dolor sit amet,<br>consectetuer adipiscing elit.</p>
    </div>
    <div class="menu-item">
      <div class="menu-item-head"><span>Banana Split</span><span class="price">8</span><span class="price">10</span><span class="price">12</span></div>
      <p class="item-desc">Lorem ipsum dolor sit amet,<br>consectetuer adipiscing elit.</p>
    </div>
    <div class="menu-item">
      <div class="menu-item-head"><span>Strawberry</span><span class="price">8</span><span class="price">10</span><span class="price">12</span></div>
      <p class="item-desc">Lorem ipsum dolor sit amet,<br>consectetuer adipiscing elit.</p>
    </div>
    <div class="menu-item">
      <div class="menu-item-head"><span>Lemon</span><span class="price">8</span><span class="price">10</span><span class="price">12</span></div>
      <p class="item-desc">Lorem ipsum dolor sit amet,<br>consectetuer adipiscing elit.</p>
    </div>
  </section>

</div>
</body>
</html>
```